Mandarin tuition, language and travel services

We need a website for a new startup company, which offers Mandarin tuition, translating and interpreting, and travel services. Our company is based in Jersey, a British channel island. We would like a creative and modern professional website. Preferably with some animations. The attached is a website, which style we would prefer:
http://www.quorvabelt.net/
We have also attached our logo for your reference
We would also like to see designs using black, red and orange, which corresponds with our logo colours. The cartoon images could be travel resorts in China, and the president of China waving to the web-browsers. Of course, we wouldn't wish to restrain the designers creativity. Any creative and interesting ideas are welcomed! We look forward to hearing from you!

Target Market(s)

school children and adults

Industry/Entity Type

It Company

Number of Pages Required

3 page

Requirements
Must have
• We would prefer a small 3 pages website, if possible. The 3 pages need to be Services, News Room, and Contact us.

```html
<!DOCTYPE html>
<html lang="en">
<head>
<meta charset="utf-8">
<title>Lantern Lingo — Mandarin Tuition, Translation &amp; Travel</title>
<link rel="stylesheet" href="https://fonts.googleapis.com/css2?family=Cinzel:wght@400;700&family=Lato:wght@400;700&family=Oswald:wght@500&display=swap">
<style>
:root{
  --charcoal:#3c3c3c;
  --black:#000;
  --ink:#141414;
  --panel:#404040;
  --red:#e30613;
  --gold:#f2c200;
  --olive:#8a7a3a;
  --white:#fff;
  --field:#cfcfcf;
  --muted:#bdbdbd;
}
*{margin:0;padding:0;box-sizing:border-box}
html,body{width:760px;height:1200px;overflow:hidden;background:var(--ink)}
body{position:relative;font-family:'Lato',sans-serif;color:var(--white)}
.abs{position:absolute}
.serif{font-family:'Cinzel',serif}

/* top bar */
.topbar{left:0;top:0;width:760px;height:44px;background:var(--charcoal);z-index:2}
.topbar .phone{left:62px;top:14px;font-size:13px;display:flex;align-items:center;gap:6px}
.topbar .mail{right:72px;top:16px;font-size:9.5px;display:flex;align-items:center;gap:6px}
.ring{width:17px;height:17px;border:1.5px solid var(--white);border-radius:50%;display:flex;align-items:center;justify-content:center}
.mainnav{left:0;top:44px;width:760px;height:24px;background:var(--black);z-index:2}
.mainnav a{position:absolute;top:0;height:24px;line-height:25px;color:var(--white);text-decoration:none;font-family:'Cinzel',serif;font-size:10.5px;letter-spacing:.6px}
.mainnav .active{background:var(--red);padding:0 15px}
.mainnav .sep{position:absolute;left:602px;top:0;width:1px;height:24px;background:#555}
.brand{left:311px;top:4px;width:100px;height:100px;border-radius:50%;background:var(--white);border:2px solid var(--black);display:flex;align-items:center;justify-content:center;text-align:center;font-family:'Oswald',sans-serif;font-size:17px;line-height:1.1;color:var(--black);z-index:10}

/* hero */
.hero{left:0;top:68px;width:760px;height:330px;background:linear-gradient(100deg,#2d3a55 0%,#b89a86 22%,#d8d3cb 45%,#a7a49a 70%,#6e6a62 100%);z-index:1}
.caption{left:382px;top:309px;width:378px;height:89px;background:rgba(40,40,40,.55);z-index:3}
.caption p{position:absolute;right:14px;font-family:'Oswald',sans-serif;font-size:20px;color:var(--white);white-space:nowrap}
.dots{right:16px;top:381px;display:flex;gap:4px;z-index:4}
.dots i{width:6px;height:6px;border-radius:50%;background:var(--white)}
.dots i:first-child{background:var(--gold)}

/* welcome */
.welcome{left:0;top:398px;width:760px;height:190px;background:radial-gradient(ellipse at 50% 40%,#2a2a2a,#0b0b0b 75%)}
.title{width:760px;left:0;text-align:center;font-family:'Cinzel',serif;font-size:21px;letter-spacing:.5px}
.divider{left:0;width:760px;height:10px}
.welcome .copy{left:72px;top:101px;width:616px;text-align:center;font-size:8.4px;line-height:15.5px;color:#e6e6e6}

/* services */
.services{left:0;top:588px;width:760px;height:288px;background:var(--panel)}
.svc{width:180px;text-align:center}
.svc .disc{margin:0 auto;width:94px;height:94px;border-radius:50%;background:var(--white);border:4px solid #2a2a2a;display:flex;align-items:center;justify-content:center}
.svc.on .disc{border-color:var(--gold)}
.svc h3{margin-top:10px;font-family:'Cinzel',serif;font-weight:400;font-size:14px;line-height:18px;letter-spacing:.5px}
.svc.on h3{color:var(--gold)}

/* news + inquiry */
.lower{left:0;top:876px;width:760px;height:202px;background:radial-gradient(ellipse at 30% 40%,#2a2a2a,#0b0b0b 80%)}
.head{font-family:'Cinzel',serif;font-size:17px;display:flex;align-items:center;gap:8px}
.rule{height:1px;background:#555}
.news{left:62px;width:300px;height:40px}
.news .thumb{position:absolute;left:0;top:0;width:48px;height:34px;background:linear-gradient(135deg,#c8b8a8,#7a5a4e 60%,#3d4f6b)}
.news h4{position:absolute;left:60px;top:0;font-size:8.2px;font-weight:700}
.news time{position:absolute;right:2px;top:0;font-size:7.6px;font-weight:700}
.news p{position:absolute;left:60px;top:12px;width:240px;font-size:7.6px;line-height:11.5px;color:#ddd}
.field{background:var(--field);color:#444;font-size:7.8px;padding:4px 4px}
.submit{left:398px;top:1036px;width:60px;height:18px;background:var(--gold);color:#222;font-weight:700;font-size:10px;text-align:center;line-height:18px}

/* footer */
.footer{left:0;top:1078px;width:760px;height:92px;background:var(--red)}
.footnav{left:0;top:20px;width:760px;text-align:center;font-size:8.6px}
.footnav span{margin:0 9px}
.contact{top:54px;display:flex;gap:8px;align-items:center;font-size:7.4px;line-height:11px}
.contact b{display:block;font-size:7.6px}
.contact .ring{width:20px;height:20px}
.base{left:0;top:1170px;width:760px;height:30px;background:var(--black)}
.base p{position:absolute;left:64px;top:10px;font-size:8px}
.social{right:70px;top:4px;display:flex;gap:4px}
.social i{width:18px;height:18px;border:1.3px solid var(--white);border-radius:50%}
</style>
</head>
<body>

<header>
  <div class="abs topbar">
    <div class="abs phone"><span class="ring"><svg width="9" height="9" viewBox="0 0 10 10"><path d="M2 1l2 2-1 1c.6 1.3 1.7 2.4 3 3l1-1 2 2-1.5 1.5C4.5 9 1 5.5.5 2.5z" fill="#fff"/></svg></span>123-456-7890</div>
    <div class="abs mail"><span class="ring" style="width:14px;height:14px"><svg width="8" height="6" viewBox="0 0 8 6"><rect x=".5" y=".5" width="7" height="5" fill="none" stroke="#fff"/><path d="M.5.5l3.5 3 3.5-3" fill="none" stroke="#fff"/></svg></span>info@lanternlingo.com</div>
  </div>
  <nav class="abs mainnav">
    <a class="active" style="left:62px">HOME</a>
    <a style="left:155px">SERVICES</a>
    <a style="left:521px">NEWS ROOM</a>
    <span class="sep"></span>
    <a style="left:622px">CONTACT US</a>
  </nav>
  <div class="abs brand">Lantern<br>Lingo</div>
</header>

<section>
  <div class="abs hero" role="img" aria-label="Photo of smiling students holding books on a university campus, with students walking in the background"></div>
  <div class="abs caption">
    <p style="top:6px">Improve Your Practical Language Skills</p>
    <p style="top:33px">We Will Help You Understand The Worlds</p>
  </div>
  <div class="abs dots"><i></i><i></i><i></i><i></i></div>
</section>

<section class="abs welcome">
  <h1 class="abs title" style="top:32px;font-weight:400">WELCOME TO LANTERN LINGO</h1>
  <svg class="abs divider" style="top:76px" viewBox="0 0 760 10">
    <line x1="232" y1="5" x2="528" y2="5" stroke="#555" stroke-width=".8"/>
    <circle cx="367" cy="5" r="3.4" fill="#e30613"/><circle cx="380" cy="5" r="4.8" fill="#e30613"/><circle cx="394" cy="5" r="3.4" fill="#e30613"/>
  </svg>
  <p class="abs copy">Lorem ipsum dolor sit amet, consectetuer adipiscing elit, sed diam nonummy nibh euismod tincidunt ut laoreet dolore magna aliquam erat volutpat. Ut wisi enim ad minim veniam, quis nostrud exerci tation ullamcorper suscipit lobortis nisl ut aliquip ex ea commodo consequat. Duis autem vel eum iriure dolor in hendrerit in vulputate velit esse molestie consequat, vel illum dolore eu feugiat nulla facilisis at vero eros et accumsan et iusto odio dignissim qui blandit praesent luptatum zzril delenit augue duis dolore te feugait nulla facilisi.</p>
</section>

<section class="abs services">
  <h2 class="abs title" style="top:36px;font-weight:400">OUR SERVICES</h2>
  <svg class="abs divider" style="top:71px" viewBox="0 0 760 10">
    <line x1="254" y1="5" x2="506" y2="5" stroke="#666" stroke-width=".8"/>
    <circle cx="367" cy="5" r="3.4" fill="#8a7a3a"/><circle cx="380" cy="5" r="4.8" fill="#8a7a3a"/><circle cx="394" cy="5" r="3.4" fill="#8a7a3a"/>
  </svg>
  <div class="abs svc on" style="left:68px;top:112px">
    <div class="disc"><svg width="46" height="40" viewBox="0 0 46 40"><rect x="4" y="4" width="38" height="26" rx="3" fill="none" stroke="#333" stroke-width="2.5"/><path d="M14 30l-4 8h26l-4-8" fill="none" stroke="#333" stroke-width="2.5"/><line x1="11" y1="13" x2="35" y2="13" stroke="#333" stroke-width="2"/><line x1="11" y1="20" x2="28" y2="20" stroke="#333" stroke-width="2"/></svg></div>
    <h3>MANDARIN<br>TUITION</h3>
  </div>
  <div class="abs svc" style="left:287px;top:112px">
    <div class="disc"><svg width="50" height="40" viewBox="0 0 50 40"><rect x="3" y="3" width="28" height="19" rx="3" fill="none" stroke="#333" stroke-width="2.5"/><path d="M9 22l-2 7 8-7" fill="none" stroke="#333" stroke-width="2.5"/><ellipse cx="34" cy="23" rx="13" ry="9" fill="#fff" stroke="#333" stroke-width="2.5"/><path d="M40 31l4 6-9-5" fill="none" stroke="#333" stroke-width="2.5"/></svg></div>
    <h3>TRANSLATING &amp;<br>INTERPRETING</h3>
  </div>
  <div class="abs svc" style="left:506px;top:112px">
    <div class="disc"><svg width="44" height="42" viewBox="0 0 44 42"><rect x="8" y="12" width="28" height="24" rx="3" fill="#333"/><rect x="16" y="5" width="12" height="8" rx="2" fill="none" stroke="#333" stroke-width="2.5"/><line x1="15" y1="14" x2="15" y2="34" stroke="#fff" stroke-width="1.6"/><line x1="29" y1="14" x2="29" y2="34" stroke="#fff" stroke-width="1.6"/><circle cx="13" cy="39" r="2.2" fill="#333"/><circle cx="31" cy="39" r="2.2" fill="#333"/></svg></div>
    <h3>TRAVEL<br>SERVICES</h3>
  </div>
</section>

<section class="abs lower">
  <div class="abs head" style="left:62px;top:24px"><svg width="16" height="16" viewBox="0 0 16 16"><rect x="1" y="3" width="14" height="12" fill="none" stroke="#fff" stroke-width="1.4"/><line x1="1" y1="6.5" x2="15" y2="6.5" stroke="#fff" stroke-width="1.4"/><line x1="4.5" y1="1" x2="4.5" y2="4.5" stroke="#fff" stroke-width="1.4"/><line x1="11.5" y1="1" x2="11.5" y2="4.5" stroke="#fff" stroke-width="1.4"/></svg>LATEST NEWS</div>
  <svg class="abs" style="left:329px;top:29px" width="34" height="12" viewBox="0 0 34 12"><circle cx="6" cy="6" r="5" fill="none" stroke="#888"/><path d="M7.5 3.5L5 6l2.5 2.5" fill="none" stroke="#888"/><circle cx="26" cy="6" r="5" fill="none" stroke="#888"/><path d="M24.5 3.5L27 6l-2.5 2.5" fill="none" stroke="#888"/></svg>
  <div class="abs rule" style="left:62px;top:56px;width:300px"></div>
  <div class="abs head" style="left:398px;top:24px"><svg width="20" height="16" viewBox="0 0 20 16"><ellipse cx="8" cy="6" rx="7" ry="5" fill="none" stroke="#fff" stroke-width="1.4"/><path d="M13 9c4 0 6 2 5 4l1 3-3-2" fill="none" stroke="#fff" stroke-width="1.4"/></svg>QUICK INQUIRY</div>
  <div class="abs rule" style="left:398px;top:56px;width:300px"></div>
</section>

<article class="abs news" style="top:950px">
  <div class="thumb" role="img" aria-label="Photo of students in a classroom"></div>
  <h4>Lorem ut perspiciatis unde omnis</h4><time>06, May, 2016</time>
  <p>Accusant doloremque laudantium, totamrem aperiam,moregil mori eaquemi ipsa quae ab illoi facilies.</p>
</article>
<div class="abs rule" style="left:62px;top:1000px;width:300px;background:#333"></div>
<article class="abs news" style="top:1016px">
  <div class="thumb" role="img" aria-label="Photo of a group of students studying together"></div>
  <h4>Lorem ut perspiciatis unde omnis iste natus</h4><time>07, May, 2016</time>
  <p>Accusant doloremque laudantium, totamrem aperiam,moregil mori eaquemi ipsa quae ab illoi facilies.</p>
</article>

<form>
  <div class="abs field" style="left:398px;top:951px;width:144px;height:18px">Your Name</div>
  <div class="abs field" style="left:554px;top:951px;width:144px;height:18px">Phone</div>
  <div class="abs field" style="left:398px;top:974px;width:300px;height:18px">Email</div>
  <div class="abs field" style="left:398px;top:997px;width:300px;height:33px">Message</div>
  <div class="abs submit">SUBMIT</div>
</form>

<footer>
  <div class="abs footer">
    <div class="abs footnav"><span>Home</span>•<span>Services</span>•<span>News Room</span>•<span>Contact us</span></div>
    <div class="abs rule" style="left:62px;top:38px;width:636px;background:rgba(255,255,255,.3)"></div>
    <div class="abs contact" style="left:78px"><span class="ring"><svg width="8" height="10" viewBox="0 0 8 10"><path d="M4 10C1 6 0 4.5 0 3.5a4 4 0 018 0C8 4.5 7 6 4 10z" fill="#fff"/><circle cx="4" cy="3.6" r="1.3" fill="#e30613"/></svg></span><div><b>LANTERN LINGO</b>123, Lorem Dolor zipcode -123 456</div></div>
    <div class="abs contact" style="left:288px"><span class="ring"><svg width="9" height="9" viewBox="0 0 10 10"><path d="M2 1l2 2-1 1c.6 1.3 1.7 2.4 3 3l1-1 2 2-1.5 1.5C4.5 9 1 5.5.5 2.5z" fill="#fff"/></svg></span><div><b>CALL US :</b>123-456-7890</div></div>
    <div class="abs contact" style="left:427px"><span class="ring"><svg width="10" height="9" viewBox="0 0 10 9"><rect x="2.5" y="0" width="5" height="3" fill="#fff"/><rect x="0" y="3" width="10" height="4" rx="1" fill="#fff"/><rect x="2.5" y="6" width="5" height="3" fill="#fff" stroke="#e30613" stroke-width=".6"/></svg></span><div><b>FAX US :</b>123-456-7890</div></div>
    <div class="abs contact" style="left:564px"><span class="ring"><svg width="9" height="7" viewBox="0 0 8 6"><rect x=".5" y=".5" width="7" height="5" fill="none" stroke="#fff"/><path d="M.5.5l3.5 3 3.5-3" fill="none" stroke="#fff"/></svg></span><div><b>EMAIL US:</b>info@lanternlingo.com</div></div>
  </div>
  <div class="abs base">
    <p>Copyright © 2016 Lantern Lingo. All Rights Reserved</p>
    <div class="abs social"><i></i><i></i><i></i><i></i></div>
  </div>
</footer>

</body>
</html>
```